Custom Header Designs - Automotive Parts - Alternator & Starter

We need 8 Header/Hero designs that will be used on our website. We are a company based in Montreal Canada and we re-manufacture Alternators and Starters for all types of vehicles. We offer a premium product and we are looking for premium designs that reflect the look of our packaging and the look of our website. Essentially we specialize in the sale and manufacture of two specific parts that go on all types of vehicles, Alternators and Starters. All text on these designs need to be editable as we will need to translate them to French once we get the source files.
Here are some websites of our competitors so you can draw some inspiration and see what our industry/business is all about:
https://www.quellorn.com/
https://www.rivetanvil.com/
Article that describes a remanufactured product, https://www.zephtrove.com/articles/starters-and-alternators-reman-vs-new.html
Our packaging is modern, sleek and professional. Our website is a B2B E-Commerce Site as well as an info site to promote our products. It is clean and minimal but we want the header/hero designs to help it stand out. Our main colors are blue and gray (as seen in our logo), but you can use whatever you like to compliment these colors.
Our packaging design was done on PixelHarbor, here is the link to that project so that you can see the packaging look and use any of the info that is from that project.
https://jobs.pixelharbor.ca/job/5820467
The 8 Header/Hero designs will be used in the following areas, I have included a brief description of what we are looking for:
1 - Homepage Header/Hero image - This will be the homepage hero image therefore it should summarize the info described below. We offer premium quality re-manufactured alternators and starters. We are a wholesaler/distributor that services major auto-part stores with these quality products.
2 - General Product Header/Hero image - This image will be used as a header where the customer can learn general info about our products and any custom work we can do. This page will have a section where you can click to learn more about our individual product lines (links to product specific pages mentioned below) and a description of the custom work we can perform. We offer a two year manufacturers warranty.
3 - Alternator Product Header/Hero image - This image will be used to showcase our Alternator Product Line. Its purpose is to promote and advertise our premium re-manufactured alternators. This page will provide detailed info about our alternator re-manufacturing process and describe why our alternators are great.
4 - Starter Product Header/Hero image - This image will be used to showcase our Starter Product Line. Its purpose is to promote and advertise our premium re-manufactured starters. This page will provide detailed info about our starter re-manufacturing process and describe why our starters are great.
5 - General Header/Hero Image - This image will be used in most of our standard pages like our terms and conditions, privacy policy, warranty policy, our company page, etc. It needs to relate to the industry but be general enough so that we could use it in multiple areas
6 - Online Ordering Header image - This image will be used in our B2B area to introduce our customers to the Online Ordering system, its purpose is to advertise and explain some of the features of the Online Ordering system.
7 - B/O Re-Manufacture & Return Header Image - This image will be used in our B2B area to explain and advertise to our customers how our Backorder/R&R process works on our website. Essentially if we do not have the remanufactured part in stock but we have the core you could put the product on Backorder and we will remanufacture it in a few hours. If for any reason (rare vehicle, old vehicle, etc.) we do not have the core we will R&R (Remanufacture and Return) the customers core for them.
8 - Bulk Ordering Form Header Image - This image will be used in our B2B area to explain and advertise to our customers how our Bulk Ordering Form works on our website.
These hero/header images will be going on a Wordpress/WooCommerce website and I am suggesting these images have a size of 1600 x 500, but we will take any other suggestions from the designers as you are the experts.
I have included a zip file that includes images of various elements that will help you in the design process.
Target Market(s)
Educate consumers about our products and attract auto supply chains to become distributors of our products.
Industry/Entity Type
Automotive Part

```html
<!DOCTYPE html>
<html lang="en">
<head>
<meta charset="utf-8">
<title>About Ampworth – Header</title>
<link rel="stylesheet" href="https://fonts.googleapis.com/css2?family=Roboto:wght@400;500;700&family=Exo+2:ital,wght@1,600;1,900&family=Montserrat:wght@600&display=swap">
<style>
  :root {
    --topbar-bg: #f5f5f5;
    --link-blue: #2b3fae;
    --text-grey: #555b61;
    --text-dark: #2a2a2a;
    --brand-blue: #1f3a9b;
    --accent-red: #e30613;
    --button-red: #c8101a;
    --hero-blue-deep: #0d2266;
    --hero-blue: #1d3fa8;
    --silver-light: #e4e5e8;
    --silver-dark: #9a9ca2;
    --photo-dark: #1a1512;
    --photo-warm: #b06a3e;
    --badge-blue: #8fd3f2;
    --white: #ffffff;
  }
  * { box-sizing: border-box; margin: 0; padding: 0; }
  html, body { width: 1200px; height: 533px; overflow: hidden; background: var(--white); }
  body { position: relative; font-family: "Roboto", Arial, sans-serif; }

  .top-bar {
    height: 25px; background: var(--topbar-bg);
    display: flex; align-items: center; padding: 0 195px 0 198px;
    font-size: 10px;
  }
  .top-bar a { color: var(--link-blue); text-decoration: none; }
  .top-bar__right { margin-left: auto; display: flex; align-items: center; gap: 0; }
  .top-bar__call { color: var(--text-grey); }
  .top-bar__call strong { color: var(--text-dark); font-weight: 700; }
  .top-bar__sep { color: var(--text-grey); margin: 0 10px; }
  .top-bar__dashboard { font-size: 8px; letter-spacing: .2px; margin-left: 20px; }
  .top-bar__lang { font-size: 7.5px; color: var(--text-dark); margin-left: 22px; display: flex; align-items: center; gap: 3px; }

  .site-header {
    height: 76px; display: flex; align-items: center;
    padding: 0 0 0 207px; position: relative;
  }
  .brand { display: flex; align-items: center; gap: 8px; width: 199px; }
  .brand__dot { width: 26px; height: 26px; border-radius: 50%; background: var(--brand-blue); }
  .brand__name { font-family: "Roboto", Arial, sans-serif; font-weight: 700; font-size: 22px; color: var(--brand-blue); }
  .main-nav { display: flex; gap: 17.5px; font-size: 11px; color: var(--text-grey); margin-top: -3px; }
  .main-nav a { color: var(--text-grey); text-decoration: none; }
  .main-nav .is-user { color: var(--link-blue); border-bottom: 1px solid var(--link-blue); padding-bottom: 2px; }
  .cart { position: relative; margin-left: 10px; margin-top: 2px; }
  .cart__badge {
    position: absolute; top: -12px; left: 14px; width: 13px; height: 13px; border-radius: 50%;
    background: var(--badge-blue); color: var(--brand-blue); font-size: 7px;
    display: flex; align-items: center; justify-content: center;
  }

  .header-rule { height: 4px; background: var(--accent-red); }
  .header-gap { height: 2px; background: var(--white); }

  .hero { position: absolute; top: 107px; left: 0; width: 1200px; height: 426px; overflow: hidden; }
  .hero__art { position: absolute; inset: 0; }
  .hero__copy { position: absolute; left: 203px; top: 70px; color: var(--white); }
  .hero__kicker { font-family: "Exo 2", sans-serif; font-style: italic; font-weight: 600; font-size: 24px; letter-spacing: .3px; }
  .hero__title { font-family: "Exo 2", sans-serif; font-style: italic; font-weight: 900; font-size: 38px; margin-top: 4px; letter-spacing: .5px; }
  .hero__button {
    display: inline-flex; align-items: center; justify-content: center;
    margin-top: 14px; width: 160px; height: 47px;
    background: linear-gradient(var(--accent-red), var(--button-red));
    border: 1.5px solid var(--white); color: var(--white); text-decoration: none;
    font-family: "Montserrat", sans-serif; font-weight: 600; font-size: 17px; letter-spacing: .3px;
  }
</style>
</head>
<body>
  <div class="top-bar">
    <a href="#">Book a Sales Consultation →</a>
    <div class="top-bar__right">
      <span class="top-bar__call">Call us now: <strong>514.555.0182</strong></span>
      <span class="top-bar__sep">|</span>
      <a href="#">Find us on the map →</a>
      <a class="top-bar__dashboard" href="#">MY AMPWORTH DASHBOARD</a>
      <span class="top-bar__lang">
        <svg width="12" height="8" viewBox="0 0 12 8"><rect width="12" height="8" fill="#243f8f"/><path d="M0 0L12 8M12 0L0 8" stroke="#fff" stroke-width="1.6"/><path d="M6 0V8M0 4H12" stroke="#fff" stroke-width="2.4"/><path d="M6 0V8M0 4H12" stroke="#d2232a" stroke-width="1.2"/></svg>
        English (English)
      </span>
    </div>
  </div>

  <header class="site-header">
    <div class="brand">
      <span class="brand__dot"></span>
      <span class="brand__name">Ampworth</span>
    </div>
    <nav class="main-nav">
      <a href="#">Home</a>
      <a href="#">Products</a>
      <a href="#">Our Company</a>
      <a href="#">Customer Resources</a>
      <a href="#">Contact Us</a>
      <a href="#">Online Ordering</a>
      <a class="is-user" href="#">Hello, administrator</a>
    </nav>
    <div class="cart">
      <svg width="15" height="15" viewBox="0 0 15 15" fill="none" stroke="#333" stroke-width="1.2"><path d="M1.5 5.5H13.5L12.5 14H2.5Z"/><path d="M4.5 5.5V4a3 3 0 0 1 6 0v1.5"/></svg>
      <span class="cart__badge">2</span>
    </div>
  </header>
  <div class="header-rule"></div>
  <div class="header-gap"></div>

  <section class="hero">
    <svg class="hero__art" width="1200" height="426" viewBox="0 0 1200 426">
      <defs>
        <linearGradient id="photoTone" x1="0" y1="0" x2="1" y2="1">
          <stop offset="0" stop-color="#2a2420"/>
          <stop offset=".45" stop-color="#6b4a35"/>
          <stop offset=".7" stop-color="var(--photo-warm)"/>
          <stop offset="1" stop-color="var(--photo-dark)"/>
        </linearGradient>
        <linearGradient id="blueTone" x1="0" y1="0" x2="1" y2="1">
          <stop offset="0" stop-color="var(--hero-blue)"/>
          <stop offset=".6" stop-color="#173391"/>
          <stop offset="1" stop-color="var(--hero-blue-deep)"/>
        </linearGradient>
        <linearGradient id="silverTone" x1="0" y1="0" x2="1" y2="0">
          <stop offset="0" stop-color="var(--silver-light)"/>
          <stop offset="1" stop-color="var(--silver-dark)"/>
        </linearGradient>
      </defs>
      <rect role="img" aria-label="Photo of hands holding a remanufactured alternator on a workbench" x="0" y="0" width="1200" height="426" fill="url(#photoTone)"/>
      <polygon points="794,0 812,0 434,426 416,426" fill="var(--accent-red)"/>
      <polygon points="755,0 794,0 416,426 370,426" fill="url(#silverTone)"/>
      <polygon points="752,0 755,0 370,426 367,426" fill="var(--white)"/>
      <polygon role="img" aria-label="Blue-tinted photo of alternator engine parts" points="0,0 752,0 367,426 0,426" fill="url(#blueTone)"/>
    </svg>
    <div class="hero__copy">
      <p class="hero__kicker">Subheadline</p>
      <h1 class="hero__title">About Ampworth</h1>
      <a class="hero__button" href="#">LEARN MORE</a>
    </div>
  </section>
</body>
</html>
```